Telepsychiatry Healthcare Services

I am a Family Medicine, Psychiatry Mental Health Nurse Practitioner, starting solo practice for mental health care for anxiety, depression, ptsd and adhd. Talk therapy with medication management if applicable. Would like to include my picture.

Target Market(s)

Children, Adolescent and Adults

Industry/Entity Type

Integrative Mental Healthcare

Requirements
Nice to have
• Mental Helath

```html
<!DOCTYPE html>
<html lang="en">
<head>
<meta charset="UTF-8">
<title>Start Your Journey to Better Mental Health Today</title>
<link href="https://fonts.googleapis.com/css2?family=Oswald:wght@500;600;700&family=Poppins:wght@400;500;600;700&display=swap" rel="stylesheet">
<style>
  :root {
    --indigo-deep: #231a6e;
    --indigo: #3a2a9a;
    --violet: #7a4fd6;
    --lavender: #b48cf0;
    --lilac-soft: #d9c7fb;
    --ink: #1e1846;
    --text: #2d2a3a;
    --white: #ffffff;
  }
  * { box-sizing: border-box; margin: 0; padding: 0; }
  html, body { width: 849px; height: 1200px; overflow: hidden; background: #ececf2; }
  .poster {
    position: relative; width: 849px; height: 1200px; overflow: hidden;
    background: var(--white); font-family: "Poppins", sans-serif; color: var(--text);
  }
  .backdrop { position: absolute; inset: 0; }
  .brand {
    position: absolute; left: 44px; top: 44px; display: flex; align-items: center; gap: 10px;
    color: var(--white); font-size: 17px; font-weight: 600; letter-spacing: .5px;
  }
  .brand-dot { width: 30px; height: 30px; border-radius: 50%; background: var(--lavender); }
  .headline {
    position: absolute; left: 50px; top: 180px; width: 440px;
    font-family: "Oswald", sans-serif; font-weight: 600; font-size: 56px; line-height: 1.1;
    color: var(--white); text-transform: uppercase; letter-spacing: .5px;
  }
  .intro {
    position: absolute; left: 52px; top: 462px; width: 400px;
    font-size: 12.5px; line-height: 1.5; color: var(--white);
  }
  .portrait-rings { position: absolute; left: 395px; top: 150px; }
  .pill {
    position: absolute; display: flex; align-items: center; justify-content: center;
    border-radius: 40px; color: var(--white); font-weight: 700; text-transform: uppercase;
    background: linear-gradient(90deg, var(--indigo), var(--violet) 60%, var(--lavender));
    font-family: "Oswald", sans-serif; letter-spacing: 1px;
  }
  .pill-services { left: 40px; top: 668px; width: 330px; height: 58px; font-size: 30px; }
  .pill-consult { left: 40px; top: 988px; width: 340px; height: 60px; font-size: 34px; }
  .services { position: absolute; left: 56px; top: 748px; width: 360px; list-style: none; }
  .services li { display: flex; align-items: flex-start; gap: 14px; margin-bottom: 12px;
    font-size: 19px; line-height: 1.17; color: var(--ink); }
  .services svg { flex: none; width: 28px; height: 28px; margin-top: 1px; }
  .approach { position: absolute; left: 470px; top: 668px; width: 345px; }
  .approach h2 { font-family: "Oswald", sans-serif; font-size: 30px; font-weight: 600;
    color: var(--indigo); letter-spacing: .5px; }
  .approach h3 { font-size: 16px; font-weight: 600; color: var(--ink); margin-top: 2px; line-height: 1.25; }
  .approach p { font-size: 15px; line-height: 1.42; margin-top: 4px; }
  .contacts { position: absolute; left: 470px; top: 968px; list-style: none; }
  .contacts li { display: flex; align-items: center; gap: 12px; font-size: 17px; margin-bottom: 10px; color: var(--ink); }
  .contacts .icon { width: 28px; height: 28px; border-radius: 50%; background: var(--indigo);
    display: flex; align-items: center; justify-content: center; }
</style>
</head>
<body>
<main class="poster">
  <svg class="backdrop" width="849" height="1200" viewBox="0 0 849 1200" aria-hidden="true">
    <defs>
      <linearGradient id="heroFade" x1="0" y1="0" x2="0" y2="1">
        <stop offset="0" stop-color="#221a6c"/>
        <stop offset="0.45" stop-color="#3b2b9c"/>
        <stop offset="1" stop-color="#8a62e0"/>
      </linearGradient>
      <linearGradient id="waveLight" x1="0" y1="0" x2="1" y2="0">
        <stop offset="0" stop-color="#c9a9f6"/>
        <stop offset="1" stop-color="#8e67e3"/>
      </linearGradient>
      <linearGradient id="footBand" x1="0" y1="0" x2="1" y2="0">
        <stop offset="0" stop-color="#3a2a9a"/>
        <stop offset="1" stop-color="#7a4fd6"/>
      </linearGradient>
    </defs>
    <path d="M0 0 H849 V600 C700 640 560 700 420 690 C260 680 120 640 0 660 Z" fill="url(#heroFade)"/>
    <path d="M0 560 C150 600 260 640 420 640 C580 640 720 600 849 560 V600 C700 660 560 700 420 695 C260 690 120 650 0 665 Z" fill="url(#waveLight)" opacity="0.7"/>
    <path d="M0 1100 C200 1065 420 1115 620 1090 C720 1078 800 1073 849 1082 V1200 H0 Z" fill="url(#waveLight)" opacity="0.6"/>
    <path d="M0 1128 C220 1100 440 1145 640 1118 C740 1106 810 1108 849 1113 V1200 H0 Z" fill="url(#footBand)"/>
  </svg>

  <div class="brand"><span class="brand-dot"></span>Serene Mind Care</div>

  <h1 class="headline">Start your journey to better mental health today</h1>

  <p class="intro">Hi, I'm [Your Full Name], a dual-certified Family Medicine and Psychiatric Mental Health Nurse Practitioner. I specialize in providing compassionate, individualized mental health care for adults and teens experiencing anxiety, depression, PTSD, and ADHD. With my experience in both physical and mental health, I offer a holistic approach to improving your overall well-being.</p>

  <svg class="portrait-rings" width="420" height="420" viewBox="0 0 420 420">
    <defs>
      <radialGradient id="portraitTone" cx="0.5" cy="0.4" r="0.6">
        <stop offset="0" stop-color="#b7a6d8"/>
        <stop offset="1" stop-color="#5b4696"/>
      </radialGradient>
    </defs>
    <circle cx="210" cy="205" r="200" fill="none" stroke="#ffffff" stroke-opacity="0.25" stroke-width="2"/>
    <path d="M40 120 A190 190 0 0 1 300 35" fill="none" stroke="#ffffff" stroke-width="6" stroke-linecap="round"/>
    <path d="M390 260 A190 190 0 0 1 230 395" fill="none" stroke="#ffffff" stroke-width="6" stroke-linecap="round"/>
    <circle cx="210" cy="205" r="172" fill="#ffffff"/>
    <circle cx="210" cy="205" r="162" fill="url(#portraitTone)" role="img" aria-label="Portrait photo of the nurse practitioner"/>
  </svg>

  <div class="pill pill-services">Service Offered</div>

  <ul class="services">
    <li><svg viewBox="0 0 30 30"><circle cx="10" cy="9" r="5" fill="#3a2a9a"/><path d="M2 26 C2 18 18 18 18 26 Z" fill="#3a2a9a"/><circle cx="22" cy="11" r="4" fill="#7a4fd6"/><path d="M16 26 C16 19 28 19 28 26 Z" fill="#7a4fd6"/></svg>Talk Therapy</li>
    <li><svg viewBox="0 0 30 30"><rect x="6" y="10" width="18" height="18" rx="3" fill="#3a2a9a"/><rect x="8" y="3" width="14" height="6" rx="2" fill="#7a4fd6"/><path d="M15 14 V24 M10 19 H20" stroke="#fff" stroke-width="2.5"/></svg>Medication Management<br>(if applicable)</li>
    <li><svg viewBox="0 0 30 30"><path d="M15 27 C4 19 2 13 5 8 C8 3 13 5 15 9 C17 5 22 3 25 8 C28 13 26 19 15 27 Z" fill="#3a2a9a"/><path d="M8 15 H12 L14 11 L17 19 L19 15 H23" stroke="#fff" stroke-width="2" fill="none"/></svg>Treatment for Anxiety,<br>Depression, PTSD, and ADHD</li>
    <li><svg viewBox="0 0 30 30"><rect x="5" y="4" width="20" height="24" rx="3" fill="#3a2a9a"/><path d="M10 16 L14 20 L21 11" stroke="#fff" stroke-width="2.5" fill="none"/></svg>Personalized care plans<br>tailored to your unique needs</li>
  </ul>

  <section class="approach">
    <h2>THERAPY APPROACH</h2>
    <h3>Talk Therapy with Medication<br>Management</h3>
    <p>I believe that every individual is unique, and so is their path to healing. That's why I provide talk therapy as a primary tool for addressing mental health challenges. When necessary, I also offer medication management to support your journey toward wellness.</p>
  </section>

  <ul class="contacts">
    <li><span class="icon"><svg width="16" height="16" viewBox="0 0 16 16"><circle cx="8" cy="8" r="3.5" fill="none" stroke="#fff" stroke-width="1.8"/><path d="M11.5 5 V9.5 C11.5 12 14.5 11 14.5 8 A6.5 6.5 0 1 0 11 13.6" fill="none" stroke="#fff" stroke-width="1.8"/></svg></span>@calmpathcare</li>
    <li><span class="icon"><svg width="14" height="14" viewBox="0 0 14 14"><path d="M3 1 L5.5 1 L6.5 4 L5 5.2 C5.8 7 7 8.2 8.8 9 L10 7.5 L13 8.5 V11 C13 12 12 13 11 13 C5.5 12.6 1.4 8.5 1 3 C1 2 2 1 3 1 Z" fill="#fff"/></svg></span>+1-555-014-2290</li>
  </ul>

  <div class="pill pill-consult">Consult Now</div>
</main>
</body>
</html>
```